Flyer für Verkauf von Nähmaschinen, Stickmaschinen und Overlock
Zielgruppe
1. Verkauf von Nähmaschinen, Stickmaschinen und Overlock.
2. Unsere Onlineshop ist www.Kornblum-Versand.de
4. Eigene Meisterwerkstatt wo alle Fabrikate repariert werden.
5. Zielgruppe = 95% Frauen
Aufgabenstellung
1. Format: DIN Maxi (23,5 x 12,5 cm Querformat, 2 Seiten)
2. Das Design soll an unseren Onlineshop www.kornblum-versand.de angelehnt sein.
3. Der Flyer soll eine Werbeaktion zum Black Friday (SILVER MAPLE DAYS) werden. 20% auf alle Neuwaren mit Gutscheincode. Unter anderem soll auf der Rückseite auch noch unsere eigene Meisterwerkstatt gezeigt werden, damit potenzielle Kunden auch wissen das wir eine Werkstatt haben.

```html
<!DOCTYPE html>
<html lang="de">
<head>
<meta charset="utf-8">
<title>Kornblum Versand – Silver Maple Days Flyer</title>
<link rel="stylesheet" href="https://fonts.googleapis.com/css2?family=Arimo:wght@400;700&family=Bebas+Neue&display=swap">
<style>
  :root{
    --stage:#3d3d3c;
    --red:#e31e24;
    --red-deep:#d21c17;
    --black:#000;
    --ink:#1d1d1b;
    --paper:#fff;
    --tear:#e6e6e6;
  }
  *{margin:0;padding:0;box-sizing:border-box}
  html,body{width:1200px;height:1200px;overflow:hidden;background:var(--stage)}
  body{position:relative;font-family:"Arimo",Arial,sans-serif}

  .flyer{position:absolute;overflow:hidden;background:var(--paper)}

  /* front side */
  .flyer--front{left:99px;top:129px;width:803px;height:427px}
  .front__band{position:absolute;left:0;top:0;width:100%;height:28px;background:var(--red-deep)}
  .front__hero{position:absolute;left:0;top:28px;width:508px;height:295px;
    background:linear-gradient(135deg,#6b7a8c 0%,#c9c9c6 45%,#8d8f92 75%,#3c3f44 100%)}
  .front__grid{position:absolute;left:513px;top:28px;width:290px;height:295px;
    display:grid;grid-template-columns:1fr 1fr;grid-template-rows:1fr 1fr 1fr;gap:4px;background:#cfcfcf}
  .tile{width:100%;height:100%}
  .tile--shop{background:linear-gradient(160deg,#f2efe9,#c7bba8)}
  .tile--foot{background:linear-gradient(160deg,#e4e6e8,#15777f)}
  .tile--screen{background:linear-gradient(160deg,#f0efee,#c9b7a3)}
  .tile--thread{background:linear-gradient(160deg,#e2572a,#d91f4b)}
  .tile--advisor{background:linear-gradient(160deg,#d9cfc0,#8a7d6c)}
  .tile--repair{background:linear-gradient(160deg,#c9cfd8,#5b6470)}
  .front__base{position:absolute;left:0;top:323px;width:100%;height:104px;background:var(--black)}

  .brand{position:absolute;display:flex;align-items:center;gap:12px;color:var(--paper);
    font-family:"Arimo",Arial,sans-serif;font-weight:700;text-transform:uppercase;line-height:0.95}
  .brand__mark{background:var(--red);flex:none}
  .front__brand{right:22px;bottom:24px;font-size:32px}
  .front__brand .brand__mark{width:44px;height:44px}

  /* back side */
  .flyer--back{left:294px;top:632px;width:805px;height:427px}
  .back__offer{position:absolute;left:0;top:0;width:100%;padding-top:12px;text-align:center;
    color:var(--paper);font-size:20px;line-height:24px;font-weight:700;z-index:3}
  .back__offer .campaign{letter-spacing:.5px}
  .back__shapes{position:absolute;inset:0;z-index:1}
  .back__photo{position:absolute;left:528px;top:107px;width:277px;height:211px;z-index:2;
    background:linear-gradient(120deg,#f4f4f2 0%,#dcdcd8 45%,#2f9a82 80%,#1f6e5c 100%)}

  .sale{position:absolute;left:29px;top:136px;width:165px;z-index:3}
  .sale__title{font-family:"Bebas Neue","Arial Narrow",sans-serif;font-weight:400;color:var(--red);
    font-size:84px;line-height:62px;letter-spacing:-1px;text-transform:uppercase;
    transform:scaleX(0.9);transform-origin:left top;white-space:nowrap}
  .sale__script{position:absolute;left:0;top:132px;width:92px;height:20px;background:var(--ink);
    border-radius:8px;transform:rotate(-6deg)}

  .back__copy{position:absolute;left:213px;top:144px;width:283px;z-index:3;
    color:var(--black);font-size:14px;line-height:17.5px;font-weight:700;text-align:justify;hyphens:manual}

  .back__contact{position:absolute;right:306px;top:366px;z-index:3;text-align:right;font-style:normal;
    color:var(--paper);font-size:14px;line-height:17.3px;font-weight:700;white-space:nowrap}
  .back__brand{right:44px;bottom:22px;z-index:3;font-size:26px}
  .back__brand .brand__mark{width:36px;height:36px}
</style>
</head>
<body>

<section class="flyer flyer--front" aria-label="Vorderseite">
  <div class="front__band"></div>
  <div class="front__hero" role="img" aria-label="Techniker justiert eine Mehrnadel-Stickmaschine in der Werkstatt"></div>
  <div class="front__grid">
    <div class="tile tile--shop" role="img" aria-label="Ladengeschäft mit Regalen und Nähmaschinen"></div>
    <div class="tile tile--foot" role="img" aria-label="Nähfuß auf petrolfarbenem Stoff"></div>
    <div class="tile tile--screen" role="img" aria-label="Touchscreen einer Stickmaschine"></div>
    <div class="tile tile--thread" role="img" aria-label="Bunte Garnrollen"></div>
    <div class="tile tile--advisor" role="img" aria-label="Beraterin an einer Nähmaschine"></div>
    <div class="tile tile--repair" role="img" aria-label="Mechaniker bei der Reparatur"></div>
  </div>
  <div class="front__base"></div>
  <div class="brand front__brand">
    <span>Kornblum<br>Versand</span>
    <span class="brand__mark"></span>
  </div>
</section>

<section class="flyer flyer--back" aria-label="Rückseite">
  <svg class="back__shapes" width="805" height="427" viewBox="0 0 805 427" aria-hidden="true">
    <rect x="0" y="0" width="805" height="427" fill="#fff"/>
    <path d="M0 0H805V115L780 110 740 106 700 112 640 100 580 107 520 96 470 104 410 93 350 99 290 90 230 98 170 92 110 101 60 96 20 104 0 100Z" fill="#e6e6e6"/>
    <path d="M0 0H805V88L770 92 730 84 690 90 640 80 600 88 560 79 510 86 460 77 410 84 360 75 310 82 260 74 220 80 180 71 130 86 100 76 60 82 20 73 0 78Z" fill="#e31e24"/>
    <path d="M0 427V305L40 300 90 312 140 302 200 314 250 300 310 310 360 296 420 306 470 294 520 304 570 296 620 314 680 300 740 312 805 302V427Z" fill="#e6e6e6"/>
    <path d="M0 427V325L45 318 95 332 150 320 210 336 260 322 320 333 370 316 430 328 480 314 530 330 580 318 630 338 690 322 750 336 805 326V427Z" fill="#1d1d1b"/>
  </svg>

  <p class="back__offer">
    Jetzt 20% auf alle Neuwaren in den <span class="campaign">Silver Maple Days</span> mit dem<br>
    Gutscheincode KVS24 in unserem Online-Shop sichern!
  </p>

  <div class="back__photo" role="img" aria-label="Mechaniker repariert eine Overlock-Maschine"></div>

  <div class="sale">
    <h1 class="sale__title">Black<br>Friday</h1>
    <div class="sale__script" role="img" aria-label="Handgeschriebener Schriftzug Sale"></div>
  </div>

  <p class="back__copy">Wir Bieten Ihnen nicht nur erstklassige Nähmaschinen, sondern auch eine indi­viduelle Beratung, um sicherzustellen, dass Sie das perfekte Modell für Ihre Bedürfnisse finden. Vertrauen Sie auf unsere Qualität und lassen Sie sich von unserem engagierten Service mit eigener Meisterwerkstatt überzeugen.</p>

  <address class="back__contact">
    Kornblum Versand · Lindenallee 17 · 84100 Mühlbach<br>
    Telefon: 49(0)8700-5531 · Telefax: 49(0)8700-5532<br>
    info@kornblum-versand.de · www.kornblum-versand.de
  </address>

  <div class="brand back__brand">
    <span>Kornblum<br>Versand</span>
    <span class="brand__mark"></span>
  </div>
</section>

</body>
</html>
```